依頼詳細
色々なホームページを参考に骨組みを作ってみました。
PDFファイルで添付しています。
2列から3列に変わると面白いのかなと思い、作りました。
もっと良い見せ方などがあれば自由に変更して頂いて構いません。

医院情報(院名・住所・診療時間)も添付資料をご覧ください。

ホームページには…
①まずは新患様に来ていただく(集客)
②医院の知名度の向上
このような効果を期待しています。

希望カラー…
建物の外装はこげ茶・白というモダンな作りです。
看板はオレンジ色です。
まだ医院が工事中で完成しておりませんが、
・完成イメージ
・現在出来上がっている院内
の写真を添付しておりますので、お色味の参考にして頂きたいです。

素材サイト:クモピクス「https://jp.kumopix.com/
このサイトの定期契約を当院で行いましたので
定期契約内で利用できる写真をデザイン内で使用してください。

他に必要なお写真がある場合には、無料で商用利用が出来るものを
ご利用頂ければと思います。

その他必要な情報などございましたらご質問ください。
楽しみにお待ちしております。宜しくお願い致します。
サイトURL
ページ数
1ページ
希望イメージ
シンプル 複雑
単色 カラフル
暗い 明るい
日常 高級
遊び心 厳粛
未来的 伝統的
女性的 男性的
希望する色
茶系、黄・オレンジ系、ベースカラーはクリーム色ぐらいのホワイトが希望です。
納品ファイル
• 高解像度JPG (.jpg)
• イラストレーター形式 (.ai)
• フォトショップ形式 (.psd)
• PNG形式 (.png)
補足説明
ランサーの皆さま

お世話になっております。
素敵なデザインをご提案頂き誠にありがとうございます。
とても嬉しいです!

期間が短く、申し訳ございません。
募集期間が延長出来るという事で、今日から1週間ほど期間を延長致します。

こちらの提出した骨組みから全く違う構成でももちろん構いませんので、
色んなパターンのデザインが見てみたいと思っています。
引き続きよろしくお願い致します。
■ 選んだ理由

一番当院のイメージに近く、一番要望に沿っているデザインだと感じたため。

■ 提案者全員のお礼・コメント

たくさんのデザインをご提案頂き、非常にうれしく思っております。
OPENに向けまずはトップデザインが決まり、わくわくしております。

この度は誠にありがとうございました。
これからも皆様のご活躍を、陰ながらではございますが、応援致しております。

```html
<!DOCTYPE html>
<html lang="ja">
<head>
<meta charset="utf-8">
<title>あおば歯科クリニック</title>
<link href="https://fonts.googleapis.com/css2?family=Noto+Sans+JP:wght@400;500;700&family=Noto+Serif+JP:wght@400;500;700&display=swap" rel="stylesheet">
<style>
:root{
  --orange:#e98a2c;
  --orange-light:#f6b563;
  --brown:#4a3426;
  --brown-mid:#6b4e3a;
  --cream:#fbf7ef;
  --beige:#f3ece0;
  --line:#ddd3c4;
  --text:#4a4038;
  --muted:#8a7f74;
  --teal:#3aa6a0;
  --pink:#e07a8c;
  --green:#6cb36b;
  --grey-bg:#ecebe8;
}
*{box-sizing:border-box;margin:0;padding:0}
html,body{width:1200px;height:4104px;overflow:hidden}
body{font-family:"Noto Sans JP",sans-serif;color:var(--text);background:var(--cream);font-size:14px;line-height:1.6}
.serif{font-family:"Noto Serif JP",serif}
.inner{width:1000px;margin:0 auto;position:relative}

/* header */
.site-header{height:132px;background:#fff}
.site-header .inner{height:132px;display:flex;align-items:center;justify-content:space-between}
.tagline{position:absolute;top:6px;left:0;font-size:11px;color:var(--muted)}
.brand{display:flex;align-items:center;gap:12px;margin-top:14px}
.brand-dot{width:34px;height:34px;border-radius:50%;background:var(--orange)}
.brand-name{font-size:30px;font-weight:700;color:var(--brown)}
.contact{margin-top:14px}
.reserve-btn{display:inline-block;background:var(--orange);color:#fff;font-size:12px;padding:3px 18px;border-radius:3px;margin-bottom:4px}
.tel{font-size:24px;font-weight:700;color:var(--brown);display:flex;align-items:center;gap:6px;line-height:1.2}
.address{font-size:11px;color:var(--muted)}
.hours{border-collapse:collapse;font-size:11px;margin-top:14px}
.hours th,.hours td{border:1px solid var(--line);padding:3px 7px;text-align:center;font-weight:400}
.hours th{background:var(--beige)}
.hours td.on{color:var(--orange)}
.hours td.off{color:#bbb}

.gnav{height:38px;background:#fff;border-top:1px solid var(--line);border-bottom:3px solid var(--orange)}
.gnav ul{list-style:none;display:flex;width:1000px;margin:0 auto;height:100%}
.gnav li{flex:1;text-align:center;line-height:35px;font-size:13px;border-right:1px solid var(--line)}
.gnav li:first-child{border-left:1px solid var(--line)}

/* hero */
.hero{height:630px;background:linear-gradient(100deg,#d9cdbc 0%,#efe7da 35%,#f8f4ec 60%,#e8e0d3 100%);position:relative}
.hero-copy{position:absolute;top:200px;left:0;right:0;text-align:center;font-size:28px;line-height:1.9;color:var(--brown)}

/* entry banners */
.entry{height:112px;background:var(--cream);padding-top:20px}
.entry .inner{display:flex;gap:60px}
.entry-card{flex:1;height:72px;border:2px solid var(--orange-light);background:#fff;display:flex;align-items:center;padding-left:30px;font-size:20px;color:var(--orange);position:relative;overflow:hidden}
.entry-card .photo{position:absolute;right:0;top:0;bottom:0;width:220px;background:linear-gradient(90deg,#fff,#f1e6dc)}

/* features */
.features{height:468px;background:linear-gradient(180deg,#514237,#3b2e25)}
.features h2{text-align:center;color:#fff;font-size:24px;font-weight:500;padding-top:36px}
.features h2 em{font-style:normal;font-size:36px;color:var(--orange-light)}
.feature-row{display:flex;justify-content:space-around;width:1000px;margin:30px auto 0}
.feature{width:230px;text-align:center;color:#fff;position:relative}
.feature .cord{width:2px;height:40px;background:#c9b9a5;margin:0 auto}
.feature .disc{width:220px;height:220px;border-radius:50%;background:radial-gradient(circle at 50% 40%,#7a5a40,#4e3726);border:3px solid #a88a6c;margin:0 auto;padding-top:28px}
.feature .num{font-size:44px;font-family:"Noto Serif JP",serif;line-height:1}
.feature .title{font-size:17px;font-weight:700;margin-top:6px;line-height:1.4}
.feature .desc{font-size:11px;color:#e9d9c4;margin-top:6px;padding:0 22px}
.feature .check{display:inline-block;font-size:10px;border:1px solid #d8c4aa;border-radius:10px;padding:0 10px;margin-top:8px}

/* pillars */
.pillars{height:400px;background:#fff;padding-top:44px}
.pillars .inner{display:flex;gap:60px}
.col{flex:1}
.col h2{text-align:center;font-size:20px;font-weight:500;color:var(--brown);margin-bottom:22px}
.promise{display:flex;align-items:center;height:54px;border:1px solid var(--line);margin-bottom:12px;background:#fff}
.promise .tag{width:54px;height:100%;color:#fff;display:flex;align-items:center;justify-content:center;font-size:13px;font-weight:700}
.promise .txt{padding-left:20px;font-size:14px;flex:1}
.promise .arrow{width:30px;color:var(--orange)}
.effort{display:flex;align-items:center;height:54px;border:1px solid var(--line);border-left:5px solid var(--orange);margin-bottom:12px;padding-left:20px;font-size:13px;line-height:1.4}
.effort small{display:block;color:var(--muted);font-size:11px}
.effort span{flex:1}
.effort .arrow{width:30px;color:var(--orange)}

/* greeting */
.greeting{height:560px;background:var(--grey-bg);padding-top:50px}
.greeting .inner{display:flex;gap:50px}
.greeting .portrait{width:340px;height:450px;background:linear-gradient(160deg,#d7d4cf,#bfbab3);display:flex;align-items:center;justify-content:center;color:#fff;font-size:14px}
.greeting .body{flex:1;padding-top:10px}
.greeting h2{font-size:22px;font-weight:500;color:var(--brown);border-bottom:1px solid #cfc8bf;padding-bottom:10px}
.greeting h3{font-size:18px;font-weight:700;color:var(--brown);margin:22px 0 16px}
.greeting p{font-size:13px;line-height:2.1;margin-bottom:12px}
.greeting .sign{text-align:right;margin-top:24px;font-size:13px}

/* troubles & services */
.care{height:390px;background:var(--cream);padding-top:36px}
.care .inner{display:flex;gap:40px}
.troubles{flex:2}
.care h2{text-align:center;font-size:19px;font-weight:500;color:var(--brown);margin-bottom:18px}
.trouble-grid{display:grid;grid-template-columns:1fr 1fr;gap:8px 16px}
.trouble{height:34px;background:#fff;border:1px solid var(--line);display:flex;align-items:center;padding:0 12px;font-size:12px;gap:10px}
.trouble .box{width:14px;height:14px;border:1.5px solid var(--orange);position:relative}
.trouble .box::after{content:"";position:absolute;left:3px;top:-2px;width:5px;height:9px;border:solid var(--orange);border-width:0 2px 2px 0;transform:rotate(40deg)}
.trouble .arrow{margin-left:auto;color:var(--orange)}
.services{flex:1}
.service{height:34px;display:flex;align-items:center;gap:14px;border-bottom:1px dotted var(--line);font-size:13px;margin-bottom:4px}
.service .ico{width:30px;height:26px;border-radius:6px;background:#f4e3cf}
.service .arrow{margin-left:auto;color:var(--orange)}

/* recruit */
.recruit{height:150px;background:var(--cream);padding-top:10px}
.recruit-box{width:1000px;margin:0 auto;height:120px;display:flex;border:1px solid var(--line)}
.recruit-box .staff{width:330px;background:linear-gradient(120deg,#e3ddd2,#cfc7ba);display:flex;align-items:center;justify-content:center;font-size:12px;color:#fff}
.recruit-box .msg{flex:1;background:var(--orange-light);display:flex;flex-direction:column;align-items:center;justify-content:center;color:#fff}
.recruit-box .msg strong{font-size:26px;font-weight:500}
.recruit-box .msg span{display:inline-block;margin-top:6px;background:#fff;color:var(--orange);padding:2px 24px;font-size:15px;font-weight:700}

/* news */
.news{height:570px;background:#fff;padding-top:50px}
.news .inner{display:flex;gap:60px}
.news-col{flex:1}
.news-col h2{text-align:center;font-size:20px;font-weight:500;color:var(--brown);padding-bottom:12px;border-bottom:2px solid var(--orange-light);margin-bottom:16px}
.news-item{border-bottom:1px dotted var(--line);padding:10px 4px;font-size:12px}
.news-item time{display:block;color:var(--muted);font-size:11px}
.more{text-align:center;margin-top:24px}
.more span{display:inline-block;border:1px solid var(--line);padding:4px 30px;font-size:12px}

/* map */
.map{height:380px;background:linear-gradient(135deg,#e9e6df,#dcd9d0)}

/* footer */
.site-footer{height:274px;background:var(--beige);padding-top:26px;position:relative}
.footer-top{display:flex;gap:30px}
.footer-info{width:380px}
.footer-info .brand{margin-top:0}
.footer-info .reserve-btn{margin-top:14px}
.footer-info .tel{font-size:22px}
.footer-info .hours{margin-top:8px}
.footer-links{flex:1;display:grid;grid-template-columns:repeat(4,1fr);gap:4px 10px;font-size:12px;margin-top:60px}
.footer-links li{list-style:none}
.footer-links li.link::before{content:"・";color:var(--orange)}
.copyright{position:absolute;left:0;right:0;bottom:0;height:24px;background:var(--brown);color:#e9dccb;font-size:10px;text-align:center;line-height:24px}
</style>
</head>
<body>

<header class="site-header">
  <div class="inner">
    <p class="tagline">三重県伊賀市の歯科医院 あおば歯科クリニック｜小児歯科・矯正・インプラント</p>
    <div class="brand"><span class="brand-dot"></span><span class="brand-name">あおば歯科クリニック</span></div>
    <div class="contact">
      <span class="reserve-btn">WEB予約はこちらから</span>
      <div class="tel">
        <svg width="20" height="20" viewBox="0 0 24 24"><path fill="#e98a2c" d="M6.6 10.8a15 15 0 0 0 6.6 6.6l2.2-2.2a1 1 0 0 1 1-.25 11.4 11.4 0 0 0 3.6.6 1 1 0 0 1 1 1V20a1 1 0 0 1-1 1A17 17 0 0 1 3 4a1 1 0 0 1 1-1h3.5a1 1 0 0 1 1 1c0 1.25.2 2.45.6 3.6a1 1 0 0 1-.25 1z"/></svg>
        0595-00-4812
      </div>
      <p class="address">〒518-0000 三重県伊賀市青葉町1-2-3</p>
    </div>
    <table class="hours">
      <tr><th>診療時間</th><th>月</th><th>火</th><th>水</th><th>木</th><th>金</th><th>土</th><th>日</th></tr>
      <tr><td>9:00〜12:30</td><td class="on">●</td><td class="on">●</td><td class="on">●</td><td class="off">/</td><td class="on">●</td><td class="on">●</td><td class="off">/</td></tr>
      <tr><td>14:00〜19:00</td><td class="on">●</td><td class="on">●</td><td class="on">●</td><td class="off">/</td><td class="on">●</td><td class="on">▲</td><td class="off">/</td></tr>
    </table>
  </div>
</header>

<nav class="gnav">
  <ul><li>トップ</li><li>医院紹介</li><li>診療内容</li><li>設備紹介</li><li>アクセス</li><li>患者様の声</li><li>数値について</li></ul>
</nav>

<section class="hero" role="img" aria-label="明るい木目と白壁の院内受付の写真">
  <p class="hero-copy serif">自分の家族にも出来る、<br>安心安全な歯科医療を目指します。</p>
</section>

<section class="entry">
  <div class="inner">
    <div class="entry-card serif">初めての方へ</div>
    <div class="entry-card serif">患者様の声<div class="photo" role="img" aria-label="笑顔の女性患者の写真"></div></div>
  </div>
</section>

<section class="features">
  <h2 class="serif">あおば歯科クリニックの<em>3</em>つの特徴</h2>
  <div class="feature-row">
    <div class="feature"><div class="cord"></div><div class="disc">
      <div class="num">1</div><div class="title">最先端の虫歯治療<br>"ルミナ"</div>
      <p class="desc">セラミック治療が短期間・最短1日で治療可能！</p><span class="check">Check ›</span></div></div>
    <div class="feature"><div class="cord"></div><div class="disc">
      <div class="num">2</div><div class="title">プチ矯正<br>見えない矯正</div>
      <p class="desc">目立たない装置で気軽に始められます</p><span class="check">Check ›</span></div></div>
    <div class="feature"><div class="cord"></div><div class="disc">
      <div class="num">3</div><div class="title">小児矯正<br>歯を抜かない歯列形成</div>
      <p class="desc">〜お子様の将来のために〜</p><span class="check">Check ›</span></div></div>
  </div>
</section>

<section class="pillars">
  <div class="inner">
    <div class="col">
      <h2 class="serif">安心できる歯医者を目指して</h2>
      <div class="promise"><span class="tag" style="background:var(--teal)">安心</span><span class="txt">カウンセリングをしっかり行います</span><span class="arrow">›</span></div>
      <div class="promise"><span class="tag" style="background:var(--pink)">充実</span><span class="txt">充実した最新機器と的確な治療</span><span class="arrow">›</span></div>
      <div class="promise"><span class="tag" style="background:var(--orange)">短縮</span><span class="txt">痛い・待ち時間・治療期間を短縮</span><span class="arrow">›</span></div>
      <div class="promise"><span class="tag" style="background:var(--green)">清潔</span><span class="txt">徹底した衛生管理</span><span class="arrow">›</span></div>
    </div>
    <div class="col">
      <h2 class="serif">当院の取り組み</h2>
      <div class="effort"><span>インプラントに不安のある方へ<small>〜安心して長く使えるために〜</small></span><span class="arrow">›</span></div>
      <div class="effort"><span>予防への取り組み<small>〜自分の歯で健康をまもるために〜</small></span><span class="arrow">›</span></div>
      <div class="effort"><span>審美歯科への取り組み<small>〜健康で美しい口元のために〜</small></span><span class="arrow">›</span></div>
      <div class="effort"><span>無痛麻酔の治療<small>〜痛いのは苦手な方へ〜</small></span><span class="arrow">›</span></div>
    </div>
  </div>
</section>

<section class="greeting">
  <div class="inner">
    <div class="portrait" role="img" aria-label="院長の写真">写真が入ります</div>
    <div class="body">
      <h2 class="serif">院長挨拶</h2>
      <h3 class="serif">ご家族皆様で安心して通える歯科医院を目指して…</h3>
      <p>この度は、私の生まれ育った地元であるこの町に歯科医院を開業することとなりました。</p>
      <p>歯医者は「痛くない」「治療を丁寧に」「長く通える」をモットーに診療を行います。<br>小さなお子様からご年配の方まで、地域の皆様に安心して通っていただけるよう、<br>最新の設備と確かな技術で、一人ひとりに寄り添った治療を心がけております。</p>
      <p>不安や疑問な点もお気軽にご相談ください。丁寧なカウンセリングを大切にし、<br>患者様が納得された上で治療を進めてまいります。スタッフ一同お待ちしております。</p>
      <p>皆さまのご家族のような歯科医院を目指してまいります。</p>
      <p class="sign">院長　青葉 一郎</p>
    </div>
  </div>
</section>

<section class="care">
  <div class="inner">
    <div class="troubles">
      <h2 class="serif">このようなことでお困りではありませんか？</h2>
      <div class="trouble-grid">
        <div class="trouble"><span class="box"></span>歯がしみる・痛む<span class="arrow">›</span></div>
        <div class="trouble"><span class="box"></span>歯茎から血が出る<span class="arrow">›</span></div>
        <div class="trouble"><span class="box"></span>子供の歯並びが心配<span class="arrow">›</span></div>
        <div class="trouble"><span class="box"></span>歯を白くしたい<span class="arrow">›</span></div>
        <div class="trouble"><span class="box"></span>歯並びが気になる<span class="arrow">›</span></div>
        <div class="trouble"><span class="box"></span>口臭が気になる<span class="arrow">›</span></div>
        <div class="trouble"><span class="box"></span>入れ歯が合わない<span class="arrow">›</span></div>
        <div class="trouble"><span class="box"></span>口内炎ができる<span class="arrow">›</span></div>
        <div class="trouble"><span class="box"></span>治療が怖い・不安<span class="arrow">›</span></div>
        <div class="trouble"><span class="box"></span>歯を失ってしまった<span class="arrow">›</span></div>
        <div class="trouble"><span class="box"></span>歯を長持ちさせたい<span class="arrow">›</span></div>
        <div class="trouble"><span class="box"></span>顎が痛い<span class="arrow">›</span></div>
        <div class="trouble"><span class="box"></span>インプラントが不安<span class="arrow">›</span></div>
        <div class="trouble"><span class="box"></span>歯ぎしりがある<span class="arrow">›</span></div>
      </div>
    </div>
    <div class="services">
      <h2 class="serif">診療項目</h2>
      <div class="service"><span class="ico"></span>一般歯科<span class="arrow">›</span></div>
      <div class="service"><span class="ico"></span>小児歯科<span class="arrow">›</span></div>
      <div class="service"><span class="ico"></span>入れ歯（義歯）<span class="arrow">›</span></div>
      <div class="service"><span class="ico"></span>口腔外科<span class="arrow">›</span></div>
      <div class="service"><span class="ico"></span>審美歯科<span class="arrow">›</span></div>
      <div class="service"><span class="ico"></span>矯正歯科<span class="arrow">›</span></div>
      <div class="service"><span class="ico"></span>インプラント<span class="arrow">›</span></div>
      <div class="service"><span class="ico"></span>予防歯科<span class="arrow">›</span></div>
    </div>
  </div>
</section>

<section class="recruit">
  <div class="recruit-box">
    <div class="staff" role="img" aria-label="スタッフの集合写真">写真が入ります</div>
    <div class="msg"><strong class="serif">私たちと一緒に働きませんか？</strong><span>歯科医師・衛生士募集</span></div>
  </div>
</section>

<section class="news">
  <div class="inner">
    <div class="news-col">
      <h2 class="serif">新着情報</h2>
      <div class="news-item"><time>2016.00.00</time>タイトルが入ります。タイトルが入ります。</div>
      <div class="news-item"><time>2016.00.00</time>タイトルが入ります。タイトルが入ります。</div>
      <div class="news-item"><time>2016.00.00</time>タイトルが入ります。タイトルが入ります。</div>
      <div class="news-item"><time>2016.00.00</time>タイトルが入ります。タイトルが入ります。</div>
      <div class="news-item"><time>2016.00.00</time>タイトルが入ります。タイトルが入ります。</div>
      <div class="more"><span>一覧を見る ›</span></div>
    </div>
    <div class="news-col">
      <h2 class="serif">新着トピックス</h2>
      <div class="news-item"><time>2016.00.00</time>タイトルが入ります。タイトルが入ります。</div>
      <div class="news-item"><time>2016.00.00</time>タイトルが入ります。タイトルが入ります。</div>
      <div class="news-item"><time>2016.00.00</time>タイトルが入ります。タイトルが入ります。</div>
      <div class="news-item"><time>2016.00.00</time>タイトルが入ります。タイトルが入ります。</div>
      <div class="news-item"><time>2016.00.00</time>タイトルが入ります。タイトルが入ります。</div>
      <div class="more"><span>一覧を見る ›</span></div>
    </div>
  </div>
</section>

<section class="map" role="img" aria-label="医院周辺の地図"></section>

<footer class="site-footer">
  <div class="inner">
    <div class="footer-top">
      <div class="footer-info">
        <div class="brand"><span class="brand-dot"></span><span class="brand-name">あおば歯科クリニック</span></div>
        <span class="reserve-btn">WEB予約はこちらから</span>
        <div class="tel">0595-00-4812</div>
        <p class="address">〒518-0000 三重県伊賀市青葉町1-2-3</p>
        <table class="hours">
          <tr><th>診療時間</th><th>月</th><th>火</th><th>水</th><th>木</th><th>金</th><th>土</th><th>日</th></tr>
          <tr><td>9:00〜12:30</td><td class="on">●</td><td class="on">●</td><td class="on">●</td><td class="off">/</td><td class="on">●</td><td class="on">●</td><td class="off">/</td></tr>
          <tr><td>14:00〜19:00</td><td class="on">●</td><td class="on">●</td><td class="on">●</td><td class="off">/</td><td class="on">●</td><td class="on">▲</td><td class="off">/</td></tr>
        </table>
      </div>
      <ul class="footer-links">
        <li class="link">トップページ</li><li class="link">一般歯科</li><li class="link">審美歯科</li><li class="link">初めての方へ</li>
        <li class="link">医院紹介</li><li class="link">小児歯科</li><li class="link">矯正歯科</li><li class="link">患者様の声</li>
        <li class="link">診療内容</li><li class="link">入れ歯</li><li class="link">インプラント</li><li class="link">新着情報</li>
        <li class="link">設備紹介</li><li class="link">口腔外科</li><li class="link">予防歯科</li><li class="link">求人情報</li>
        <li class="link">アクセス</li><li></li><li></li><li></li>
      </ul>
    </div>
  </div>
  <p class="copyright">©2016 Aoba Dental Clinic All Rights Reserved.</p>
</footer>

</body>
</html>
```